Global Expert Network Firm needs business card design

We need business card design for a new company based in Seoul, South Korea called 'Corwell Insight Partners'. We recruit industry experts covering all countries and connect our client and recruited expert by phone, face-to-face meetings and etc. We are a global expert network firm that is focused on delivering high-quality experts to our clients throughout the world. Our clients include multinational corporations, global consulting firms, private equity firms, venture capital firms, asset management companies.
We have made new logo and please find attachment.(Please use new logo)
Target Market(s)
Global Consulting Firms, Investment Firms, Private Equity Firms, Venture Capital Firms.
Industry/Entity Type
Recruitment
Contact Information for Business Card
We need two Languages (English and Korean Version).
The front is Korean and the back is English version.
[The back] [English]
Company Name: Corwell Insight Partners, Inc.
CEO Name: Daniel Park
Address: #507, Hanbit Bldg, 82 Maebongsan-ro, Dobong-gu, Seoul, 01327, Korea
Tel. +82 2 718 4052
Fax. +82 2 864 1097
Mobile. +82 10 7264 8815
Email: daniel@corwellip.com
Web: www.corwellip.com
[The front] [Korean] => Described in same order as English version.
회사명: 코웰인사이트파트너스(주)
대표이사: 박도현
주소: 서울시 도봉구 매봉산로 82 한빛빌딩 507호
Tel. 02 718 4052
Fax. 02 864 1097
Mobile. 010 7264 8815
Web: www.corwellip.com
Look and feel
Each slider illustrates characteristics of the customer's brand and the style your logo design should communicate.

```html
<!DOCTYPE html>
<html lang="ko">
<head>
<meta charset="utf-8">
<title>Corwell Insight Partners – Business Card</title>
<link rel="stylesheet" href="https://fonts.googleapis.com/css2?family=Oswald:wght@300;400;500;600&family=Noto+Sans+KR:wght@300;400&display=swap">
<style>
  :root {
    --cyan: #5ffdfd;
    --cyan-light: #8ff7f5;
    --grey: #7b8a8b;
    --icon-dark: #3f4c50;
    --band-black: #050808;
    --white: #ffffff;
    --bg-start: #0f1213;
    --bg-end: #9a9c9d;
  }
  * { margin: 0; padding: 0; box-sizing: border-box; }
  html, body { width: 1200px; height: 1200px; overflow: hidden; }
  body {
    position: relative;
    background: linear-gradient(115deg, var(--bg-start) 20%, var(--bg-end) 100%);
    font-family: "Oswald", sans-serif;
  }
  .card {
    position: absolute;
    left: 210px;
    width: 780px;
    height: 419px;
    background: var(--white);
    overflow: hidden;
  }
  .card--front { top: 134px; }
  .card--back { top: 642px; }
  .card__shapes { position: absolute; inset: 0; }
  .side-label {
    position: absolute;
    left: 0; width: 1200px;
    text-align: center;
    color: var(--white);
    font-family: "Oswald", sans-serif;
    font-weight: 600;
    font-size: 40px;
  }
  .side-label--front { top: 572px; }
  .side-label--back { top: 1080px; }

  .company-band {
    position: absolute;
    left: 0; top: 65px;
    width: 345px; height: 77px;
    display: flex; flex-direction: column;
    align-items: center; justify-content: center;
    color: var(--cyan);
    line-height: 1.1;
    text-align: center;
  }
  .company-band__ko { font-family: "Noto Sans KR", sans-serif; font-weight: 400; font-size: 24px; letter-spacing: 1px; }
  .company-band__ko-label { font-family: "Noto Sans KR", sans-serif; font-weight: 300; font-size: 24px; letter-spacing: 3px; }
  .company-band__en { font-family: "Oswald", sans-serif; font-weight: 500; font-size: 22px; white-space: nowrap; }
  .company-band__en-label { color: var(--white); font-family: "Oswald", sans-serif; font-weight: 300; font-size: 21px; }

  .brand-mark {
    position: absolute;
    left: 90px; top: 236px;
    width: 240px;
    display: flex; flex-direction: column; align-items: center;
    gap: 10px;
  }
  .brand-mark__dot {
    width: 78px; height: 78px; border-radius: 50%;
    background: var(--cyan);
  }
  .brand-mark__name {
    font-family: "Oswald", sans-serif;
    font-weight: 500;
    font-size: 22px;
    color: var(--icon-dark);
    text-align: center;
    line-height: 1.1;
    white-space: nowrap;
  }

  .ceo-line {
    position: absolute;
    right: 46px; top: 14px;
    color: var(--cyan);
    font-family: "Oswald", sans-serif;
    font-weight: 300;
    font-size: 31px;
    white-space: nowrap;
  }
  .ceo-line--ko { font-family: "Noto Sans KR", sans-serif; font-weight: 300; font-size: 28px; letter-spacing: 3px; top: 12px; }
  .ceo-line strong { font-weight: 500; }

  .contact-icon { position: absolute; left: 364px; width: 62px; height: 62px; }
  .contact-text {
    position: absolute;
    left: 434px;
    color: var(--cyan);
    font-family: "Oswald", sans-serif;
    font-weight: 300;
    white-space: nowrap;
    line-height: 1;
  }
  .contact-text--address-ko { font-family: "Noto Sans KR", sans-serif; font-weight: 400; font-size: 20px; letter-spacing: -1px; top: 76px; transform: scaleX(0.82); transform-origin: left; }
  .contact-text--address-en { font-size: 17px; top: 76px; left: 430px; width: 340px; line-height: 1.35; text-align: center; }
  .contact-text--phones { font-size: 17px; top: 144px; line-height: 1.4; }
  .contact-text--email { font-size: 30px; top: 232px; left: 432px; }
  .contact-text--web { font-size: 35px; top: 310px; left: 432px; }

  .icon-pin { top: 59px; }
  .icon-phone { top: 139px; }
  .icon-mail { top: 220px; }
  .icon-web { top: 303px; }
</style>
</head>
<body>

<svg width="0" height="0" style="position:absolute">
  <defs>
    <symbol id="card-shapes" viewBox="0 0 780 419">
      <path d="M0 0 H295 C160 40 70 180 0 419 Z" fill="var(--cyan)"/>
      <path d="M150 0 H230 C120 50 40 200 0 419 L0 360 C30 200 80 80 150 0 Z" fill="var(--cyan-light)"/>
      <path d="M0 142 C10 280 6 360 6 419 L0 419 Z" fill="var(--cyan-light)"/>
      <path d="M20 142 C30 230 10 330 4 419 L0 419 L0 142 Z" fill="var(--white)"/>
      <path d="M0 142 H345 L76 192 Z" fill="var(--grey)"/>
      <path d="M276 419 L366 382 H780 V419 Z" fill="var(--cyan)"/>
      <path d="M320 419 L366 400 H780 V419 Z" fill="var(--cyan-light)"/>
      <rect x="0" y="65" width="345" height="77" fill="var(--band-black)"/>
    </symbol>
    <symbol id="icon-pin" viewBox="0 0 62 62">
      <circle cx="31" cy="31" r="31" fill="var(--icon-dark)"/>
      <path d="M31 10 C21 10 15 17 15 25 C15 35 31 52 31 52 C31 52 47 35 47 25 C47 17 41 10 31 10 Z" fill="var(--cyan)"/>
      <circle cx="31" cy="25" r="6" fill="var(--icon-dark)"/>
    </symbol>
    <symbol id="icon-phone" viewBox="0 0 62 62">
      <circle cx="31" cy="31" r="31" fill="var(--icon-dark)"/>
      <path d="M18 14 L25 13 L28 23 L23 27 C25 34 29 39 35 42 L39 37 L49 41 L48 48 C44 52 36 51 28 45 C20 38 14 28 14 21 C14 18 15 16 18 14 Z" fill="var(--cyan)"/>
    </symbol>
    <symbol id="icon-mail" viewBox="0 0 62 62">
      <circle cx="31" cy="31" r="31" fill="var(--icon-dark)"/>
      <rect x="9" y="18" width="44" height="27" fill="var(--cyan)"/>
      <path d="M9 18 L31 34 L53 18" fill="none" stroke="var(--icon-dark)" stroke-width="2.5"/>
    </symbol>
    <symbol id="icon-web" viewBox="0 0 62 62">
      <circle cx="31" cy="31" r="31" fill="var(--icon-dark)"/>
      <g fill="none" stroke="var(--cyan)" stroke-width="3">
        <circle cx="31" cy="31" r="21"/>
        <ellipse cx="31" cy="31" rx="9" ry="21"/>
        <line x1="31" y1="10" x2="31" y2="52"/>
        <line x1="10" y1="31" x2="52" y2="31"/>
        <line x1="14" y1="21" x2="48" y2="21"/>
        <line x1="14" y1="41" x2="48" y2="41"/>
      </g>
    </symbol>
  </defs>
</svg>

<section class="card card--front" lang="ko">
  <svg class="card__shapes" viewBox="0 0 780 419"><use href="#card-shapes"/></svg>
  <div class="company-band">
    <span class="company-band__ko">코웰인사이트파트너스(주)</span>
    <span class="company-band__ko-label">회사명:</span>
  </div>
  <div class="brand-mark">
    <span class="brand-mark__dot"></span>
    <span class="brand-mark__name">Corwell Insight Partners</span>
  </div>
  <div class="ceo-line ceo-line--ko">대표이사: 박도현</div>
  <svg class="contact-icon icon-pin"><use href="#icon-pin"/></svg>
  <div class="contact-text contact-text--address-ko">주소: 서울시 도봉구 매봉산로 82 한빛빌딩 507호</div>
  <svg class="contact-icon icon-phone"><use href="#icon-phone"/></svg>
  <div class="contact-text contact-text--phones">Tel. 02 718 4052<br>Fax. 02 864 1097<br>Mobile. 010 7264 8815</div>
  <svg class="contact-icon icon-mail"><use href="#icon-mail"/></svg>
  <div class="contact-text contact-text--email">Email: daniel@corwellip.com</div>
  <svg class="contact-icon icon-web"><use href="#icon-web"/></svg>
  <div class="contact-text contact-text--web">Web: www.corwellip.com</div>
</section>
<div class="side-label side-label--front">FRONT</div>

<section class="card card--back" lang="en">
  <svg class="card__shapes" viewBox="0 0 780 419"><use href="#card-shapes"/></svg>
  <div class="company-band">
    <span class="company-band__en">CORWELL INSIGHT PARTNERS, INC.</span>
    <span class="company-band__en-label">COMPANY NAME</span>
  </div>
  <div class="brand-mark">
    <span class="brand-mark__dot"></span>
    <span class="brand-mark__name">Corwell Insight Partners</span>
  </div>
  <div class="ceo-line"><strong>CEO Name:</strong> Daniel Park</div>
  <svg class="contact-icon icon-pin"><use href="#icon-pin"/></svg>
  <div class="contact-text contact-text--address-en">Address:#507, Hanbit Bldg, 82 Maebongsan-ro,<br>Dobong-gu, Seoul, 01327, Korea</div>
  <svg class="contact-icon icon-phone"><use href="#icon-phone"/></svg>
  <div class="contact-text contact-text--phones">Tel. +82 2 718 4052<br>Fax. +82 2 864 1097<br>Mobile. +82 10 7264 8815</div>
  <svg class="contact-icon icon-mail"><use href="#icon-mail"/></svg>
  <div class="contact-text contact-text--email">Email: daniel@corwellip.com</div>
  <svg class="contact-icon icon-web"><use href="#icon-web"/></svg>
  <div class="contact-text contact-text--web">Web: www.corwellip.com</div>
</section>
<div class="side-label side-label--back">BACK</div>

</body>
</html>
```